Design a Sleek, Modern Insert Card for a Wellness-Inspired Clinical Kit

We are looking for a sleek, professional insert card design to include inside our KINDLE Trial Boost kits — curated wellness pouches that will be sent to clinical research coordinators, physicians, and nurses participating in our KINDLE clinical study.
This insert should visually reflect the TALMOR Biologics and KINDLE brands (logos attached) — clean, modern, and cohesive — and serve as a small note of appreciation for their work.
Insert Text (exact wording to include):
Everything inside was chosen to fuel your focus, KINDLE your energy, and support your work advancing disc restoration.
Design Requirements:
Size: Small insert card that fits neatly inside a zippered pouch (approx. 4” x 6” or similar).
Orientation: Landscape
Logos:
KINDLE logo
TALMOR Biologics logo
(Both should be tastefully included and balanced within the design.)
Color Palette:
Shades of blue (from the KINDLE logo)
Shades of green (from the TALMOR logo)
Design Style:
Modern, clean, and minimalistic
Professional and medical, but still visually engaging
Premium feel (this will be part of an elegant, high-end kit)
Typography:
Easy to read, sans-serif fonts (open to designer’s creative judgment)
Should align with a clinical or wellness aesthetic (not overly corporate or decorative)
Examples of brand aesthetics that inspire us: Pebble packaging, Hush app, Brisk Grains, or QRVO hydration branding
Target Market(s)
Physicians & nurses
Industry/Entity Type
Medical

```html
<!DOCTYPE html>
<html lang="en">
<head>
<meta charset="utf-8">
<title>KINDLE Trial Boost – Insert Card</title>
<link href="https://fonts.googleapis.com/css2?family=Montserrat:wght@400;700&display=swap" rel="stylesheet">
<style>
  :root {
    --page-bg: #e9e9e9;
    --card-bg: #f7f7f6;
    --ink: #1d1d1f;
    --navy: #1a1f4e;
    --green: #6cb33f;
    --teal: #66c6b9;
    --wordmark: #3a3a3c;
  }
  * { margin: 0; padding: 0; box-sizing: border-box; }
  html, body {
    width: 1200px;
    height: 1200px;
    overflow: hidden;
    background: var(--page-bg);
  }
  body {
    display: flex;
    align-items: center;
    justify-content: center;
    font-family: "Montserrat", sans-serif;
  }
  .insert-card {
    position: relative;
    width: 1080px;
    height: 720px;
    background: var(--card-bg);
    box-shadow: 0 18px 40px rgba(0, 0, 0, 0.18);
    overflow: hidden;
  }
  .message {
    position: absolute;
    top: 288px;
    left: 0;
    right: 0;
    text-align: center;
    font-size: 28px;
    line-height: 37px;
    font-weight: 400;
    color: var(--ink);
    letter-spacing: -0.2px;
  }
  .message .highlight {
    color: var(--green);
    font-weight: 700;
  }
  .divider {
    position: absolute;
    top: 418px;
    left: 50%;
    width: 151px;
    height: 2px;
    margin-left: -75px;
    background: var(--navy);
  }
  .brand-row {
    position: absolute;
    left: 40px;
    top: 631px;
    width: 410px;
    height: 63px;
    display: flex;
    align-items: center;
    gap: 34px;
  }
  .brand-name {
    font-family: "Montserrat", sans-serif;
    font-weight: 700;
    font-size: 26px;
    letter-spacing: 0.2px;
    color: var(--wordmark);
    white-space: nowrap;
  }
  .accent-band {
    position: absolute;
    left: 479px;
    right: 0;
    top: 631px;
    height: 63px;
    background: var(--teal);
  }
</style>
</head>
<body>
  <main class="insert-card">
    <p class="message">
      Everything inside was chosen to fuel your focus,<br>
      <span class="highlight">KINDLE</span> your energy, and support your<br>
      work advancing disc restoration.
    </p>
    <div class="divider"></div>
    <div class="brand-row">
      <span class="brand-name">KINDLE</span>
      <span class="brand-name">TALMOR Biologics</span>
    </div>
    <div class="accent-band"></div>
  </main>
</body>
</html>
```